Modern card design needed for building development company

We are looking for a sharp modern new look for our business cards.
We are a New Zealand based company called TKV Ventures NZ LTD that specialises in subdividing large sections, housing and commercial buildings.
We have attached a photo of the current logo and would like to see it improved somehow as it looks a bit dated.
We are open to any colours.

Target Market(s)

Investors, Property buyers

Industry/Entity Type

Investment

Contact Information for Business Card

TKV VENTURES NZ LTD
www.tkvventuresnz.co.nz

Howard Pennick
Phone +64 21 843 192
Email hdpennick@fernmail.co.nz

Font styles to use
Serif
Sans Serif

Colors
0792cd
33a6d7
85cae6
6b449b
886aae
f04a50
ec1f27
f37122
f68d4d

Requirements
Must have
• Please try and make the logo more modern or if you have a similar one we would like to see it.

```html
<!DOCTYPE html>
<html lang="en">
<head>
<meta charset="utf-8">
<title>TKV Ventures NZ LTD – Business Card</title>
<link href="https://fonts.googleapis.com/css2?family=Work+Sans:wght@400;500;600&display=swap" rel="stylesheet">
<style>
  :root {
    --page-bg: #e9eaec;
    --brand-blue: #1a94d2;
    --brand-blue-light: #33a6d7;
    --card-dark: #1d1e21;
    --card-grey: #8a8b8e;
    --text-white: #ffffff;
    --text-soft: #dfe3e6;
  }
  * { box-sizing: border-box; margin: 0; padding: 0; }
  html, body {
    width: 1200px;
    height: 1000px;
    overflow: hidden;
    background: var(--page-bg);
    font-family: "Work Sans", Arial, sans-serif;
  }
  .canvas {
    position: relative;
    width: 1200px;
    height: 1000px;
  }
  .card {
    position: absolute;
    left: 320px;
    width: 560px;
    height: 320px;
    border-radius: 18px;
    overflow: hidden;
    box-shadow: 0 10px 30px rgba(0,0,0,0.18);
  }

  /* Front */
  .card--front {
    top: 150px;
    background: var(--brand-blue);
    display: flex;
    align-items: center;
    justify-content: center;
  }
  .brand {
    display: flex;
    flex-direction: column;
    align-items: center;
    color: var(--text-white);
    font-weight: 500;
  }
  .brand__mark {
    width: 46px;
    height: 46px;
    border: 2px solid currentColor;
    margin-bottom: 18px;
  }
  .brand__name {
    font-size: 30px;
    letter-spacing: 1px;
    line-height: 1.1;
  }
  .brand__suffix {
    font-size: 11px;
    letter-spacing: 4px;
    margin-top: 8px;
  }
  .brand__rule {
    width: 180px;
    height: 1px;
    background: currentColor;
    margin-top: 10px;
    opacity: 0.8;
  }

  /* Back */
  .card--back {
    top: 530px;
    background: var(--card-dark);
  }
  .card--back .brand {
    position: absolute;
    left: 40px;
    top: 90px;
    width: 210px;
    color: var(--brand-blue);
  }
  .card--back .brand__mark { width: 40px; height: 40px; margin-bottom: 16px; }
  .card--back .brand__name { font-size: 21px; }
  .card--back .brand__rule { width: 140px; }
  .divider {
    position: absolute;
    left: 282px;
    top: 70px;
    width: 2px;
    height: 130px;
    background: var(--brand-blue);
  }
  .contact {
    position: absolute;
    left: 312px;
    top: 82px;
    color: var(--text-white);
  }
  .contact__name {
    font-size: 22px;
    font-weight: 600;
    letter-spacing: 0.3px;
    margin-bottom: 22px;
  }
  .contact__row {
    display: flex;
    align-items: center;
    gap: 10px;
    font-size: 14px;
    color: var(--text-soft);
    margin-bottom: 6px;
  }
  .contact__icon { width: 11px; height: 11px; flex: none; }
  .footer-band {
    position: absolute;
    left: 0;
    bottom: 0;
    width: 100%;
    height: 52px;
  }
  .website {
    position: absolute;
    right: 26px;
    bottom: 10px;
    font-size: 14px;
    color: var(--text-white);
  }
  .website strong { font-weight: 600; }
</style>
</head>
<body>
<main class="canvas">

  <section class="card card--front" aria-label="Business card front">
    <div class="brand">
      <span class="brand__mark"></span>
      <span class="brand__name">TKV VENTURES</span>
      <span class="brand__suffix">NZ LTD</span>
      <span class="brand__rule"></span>
    </div>
  </section>

  <section class="card card--back" aria-label="Business card back">
    <div class="brand">
      <span class="brand__mark"></span>
      <span class="brand__name">TKV VENTURES</span>
      <span class="brand__suffix">NZ LTD</span>
      <span class="brand__rule"></span>
    </div>

    <span class="divider"></span>

    <div class="contact">
      <h1 class="contact__name">HOWARD PENNICK</h1>
      <p class="contact__row">
        <svg class="contact__icon" viewBox="0 0 12 12" aria-hidden="true">
          <path d="M2.5 1 L4.5 1 L5.2 3.5 L4 4.4 Q5 6.8 7.6 8 L8.5 6.8 L11 7.5 L11 9.5 Q10.6 11 9 11 Q1 10 1 2.6 Q1.2 1 2.5 1 Z" fill="var(--brand-blue)"/>
        </svg>
        +64 21 843 192
      </p>
      <p class="contact__row">
        <svg class="contact__icon" viewBox="0 0 12 12" aria-hidden="true">
          <rect x="1" y="2.5" width="10" height="7" fill="none" stroke="var(--brand-blue)" stroke-width="1.3"/>
          <path d="M1 2.5 L6 6.5 L11 2.5" fill="none" stroke="var(--brand-blue)" stroke-width="1.3"/>
        </svg>
        hdpennick@fernmail.co.nz
      </p>
    </div>

    <svg class="footer-band" viewBox="0 0 560 52" preserveAspectRatio="none" aria-hidden="true">
      <polygon points="0,44 350,38 346,52 0,52" fill="var(--card-grey)"/>
      <polygon points="380,22 560,22 560,52 350,52" fill="var(--brand-blue)"/>
    </svg>
    <p class="website">www.<strong>tkvventuresnz.co.nz</strong></p>
  </section>

</main>
</body>
</html>
```